Car wrap desgin Talvin

We’d like new design proposals for passenger cars (KM Dorvane & Brčka Ulvaro eX). Both vehicles are white. I don’t want the entire car to be wrapped in yellow. more informations about us, you will find under: https://www.talviiiin.ch/home

Less is more. Keep it simple, clean, and stylish - and only with yellow ond black as color beside the with car

```html
<!DOCTYPE html>
<html lang="de">
<head>
<meta charset="utf-8">
<title>Talvin – Fahrzeugbeschriftung</title>
<link rel="stylesheet" href="https://fonts.googleapis.com/css2?family=Poppins:wght@600;700;800&display=swap">
<style>
  :root {
    --wrap-yellow: #f2e000;
    --wrap-black: #0d0d0d;
    --canvas-bg: #ffffff;
  }
  html, body {
    margin: 0;
    padding: 0;
    width: 1200px;
    height: 1200px;
    overflow: hidden;
    background: var(--canvas-bg);
  }
  .wrap-design {
    display: block;
    width: 1200px;
    height: 1200px;
  }
  .band-yellow, .roof-accent { fill: var(--wrap-yellow); }
  .band-black, .diagonal-stripe { fill: var(--wrap-black); }
  .phone-number {
    font-family: "Poppins", sans-serif;
    font-weight: 700;
    font-size: 30px;
    fill: var(--wrap-black);
    letter-spacing: 0.5px;
  }
  .web-address {
    font-family: "Poppins", sans-serif;
    font-weight: 600;
    font-size: 22px;
    fill: var(--wrap-black);
  }
  .brand-name {
    font-family: "Poppins", sans-serif;
    font-weight: 800;
    font-size: 118px;
    fill: var(--wrap-black);
    letter-spacing: 2px;
  }
  .tagline {
    font-family: "Poppins", sans-serif;
    font-weight: 600;
    font-size: 34px;
    fill: var(--wrap-yellow);
    letter-spacing: 1px;
  }
</style>
</head>
<body>
<svg class="wrap-design" viewBox="0 0 1200 1200" xmlns="http://www.w3.org/2000/svg">
  <!-- roof accent -->
  <polygon class="roof-accent" points="1052,392 1082,392 1074,420 1044,420"/>

  <!-- main yellow band with rising stripe -->
  <polygon class="band-yellow" points="150,632 1000,632 1030,508 1058,508 958,756 112,756"/>

  <!-- black tagline band -->
  <polygon class="band-black" points="112,756 958,756 930,822 118,822"/>

  <!-- black diagonal stripe -->
  <path class="diagonal-stripe" d="M1078,534 Q1084,516 1100,516 Q1118,518 1112,536 L1000,744 L964,744 Z"/>

  <!-- contact line -->
  <text class="phone-number" x="188" y="610">+41 41 380 72 16</text>
  <text class="web-address" x="640" y="604">www.talviiiin.ch</text>

  <!-- brand name -->
  <text class="brand-name" x="185" y="738">TALVIN</text>

  <!-- tagline -->
  <text class="tagline" x="524" y="801" text-anchor="middle">HAUSTECHNIK + BAUSPENGLEREI</text>
</svg>
</body>
</html>
```